Need business cards for our e-assessment business

We need professional looking business cards for our e-assessment business based in Europe. Our company is called Velmora.

You can just use sample name and addresses.

The colours we use are:

#70abe4 (blue)
#FF6600 (orange)

The back side should say: Testing made effortless

This is the print-shop we are using. Please look at the link for info about formats: http://nl.pribbly-print.com/help/faq/using-my-own-artwork.html

Target Market(s)

Target market is education and large corporations

Industry/Entity Type

Business

```html
<!DOCTYPE html>
<html lang="en">
<head>
<meta charset="utf-8">
<title>Velmora business cards</title>
<link rel="stylesheet" href="https://fonts.googleapis.com/css2?family=Barlow:wght@400;500&display=swap">
<style>
  :root {
    --orange: #e25c00;
    --accent-orange: #ff6600;
    --blue: #70abe4;
    --ink: #3a3a3a;
    --paper: #f4f4f2;
    --backdrop: #e6e6e6;
    --tagline: #f6e6da;
    --badge: #ecebea;
  }
  * { margin: 0; padding: 0; box-sizing: border-box; }
  html, body { width: 1200px; height: 800px; overflow: hidden; }
  body {
    background: var(--backdrop);
    font-family: "Barlow", Arial, sans-serif;
    color: var(--ink);
    position: relative;
  }
  .card { position: absolute; }
  .card-back {
    left: 378px; top: 75px; width: 475px; height: 303px;
    background: var(--orange);
  }
  .card-back .badge {
    position: absolute; left: 76px; top: 113px;
    width: 76px; height: 76px; border-radius: 50%;
    background: var(--badge);
  }
  .card-back .tagline {
    position: absolute; left: 176px; top: 141px;
    font-size: 17px; letter-spacing: 1.3px;
    color: var(--tagline); line-height: 1;
  }
  .card-front {
    left: 376px; top: 417px; width: 478px; height: 311px;
    background: var(--paper);
  }
  .brand { position: absolute; left: 42px; top: 24px; display: flex; align-items: center; }
  .brand-mark {
    width: 78px; height: 78px; border-radius: 50%;
    background: var(--accent-orange);
  }
  .brand-name {
    margin-left: 20px; font-size: 56px; font-weight: 400;
    color: var(--ink); line-height: 1; letter-spacing: -0.5px;
    margin-top: -4px;
  }
  .contact { position: absolute; left: 42px; top: 144px; }
  .person { font-size: 21px; letter-spacing: 0.3px; line-height: 1; }
  .person .role { font-size: 15px; letter-spacing: 0.8px; margin-left: 10px; }
  .details { margin-top: 10px; font-size: 13.5px; line-height: 17px; letter-spacing: 0.5px; }
  .address { margin-top: 10px; font-size: 13.5px; line-height: 17px; letter-spacing: 0.5px; }
  .website {
    margin-top: 16px; font-size: 13.5px; letter-spacing: 0.5px;
    color: var(--blue); display: flex; align-items: center;
  }
  .website::before {
    content: ""; width: 6px; height: 6px; border-radius: 50%;
    background: var(--accent-orange); margin-right: 13px; margin-left: 2px;
  }
</style>
</head>
<body>
  <section class="card card-back">
    <div class="badge"></div>
    <p class="tagline">Testing made effortless</p>
  </section>

  <section class="card card-front">
    <div class="brand">
      <div class="brand-mark"></div>
      <span class="brand-name">velmora</span>
    </div>
    <div class="contact">
      <p class="person">Maarten Oldervelt<span class="role">MANAGER</span></p>
      <div class="details">
        <p>MOBILE&nbsp; 0150 7312846&nbsp; | &nbsp;PHONE&nbsp; 0655 842 1907</p>
        <p>EMAIL&nbsp; oldervelt@velmora.nl</p>
      </div>
      <div class="address">
        <p>Kastanjelaan 48, 2594 BK &nbsp;'S-Gravenhage</p>
        <p>NETHERLANDS</p>
      </div>
      <p class="website">www.velmora.nl</p>
    </div>
  </section>
</body>
</html>
```